Song ( Single ) Cover for a new track

We are looking for a cover for the initial release of our single. The song is called " Glimmer " .
This a pop track
The artist's name is " Relna " a 16 years girls
Be Creative when it comes to color and etc.. We have three images that can be used and at the end will chose one to use.
The cover will be used for digital distribution on different platform like : Tunevox, Melor, Sonarq and etc...

We do like the idea of word " Glimmer "

We would like a design that is attention grabbing ( For children, youth and adult ) so that it will catch the attention of anyone that walks by or sees it in any place.

Target Market(s)

16 +

Font styles to use
Serif
Sans Serif
Script

Requirements
Must have
• The image of the artist provided on the three i mages
Nice to have
• - Photo or detailed freehand drawing for the main picture
Should not have
• no copyrighted materials

```html
<!DOCTYPE html>
<html lang="en">
<head>
<meta charset="utf-8">
<title>Glimmer – Relna</title>
<link rel="stylesheet" href="https://fonts.googleapis.com/css2?family=Montserrat:wght@600&display=swap">
<style>
  :root {
    --cyan: #03e1e2;
    --ink: #000000;
    --yellow: #fff200;
    --skin: #e8872e;
    --denim: #1d6f86;
  }
  html, body {
    margin: 0;
    padding: 0;
    overflow: hidden;
    background: var(--cyan);
  }
  .cover {
    position: relative;
    width: 1200px;
    height: 801px;
    overflow: hidden;
    background: var(--cyan);
    font-family: "Montserrat", "Helvetica Neue", Arial, sans-serif;
  }
  .band {
    position: absolute;
    background: var(--ink);
  }
  .band--top { left: 640px; top: 0; width: 560px; height: 23px; }
  .band--top-post { left: 640px; top: 0; width: 24px; height: 200px; }
  .band--left { left: 0; top: 186px; width: 450px; height: 23px; }
  .band--right { left: 980px; top: 591px; width: 220px; height: 23px; }
  .band--foot { left: 0; top: 778px; width: 180px; height: 23px; }
  .artist-photo {
    position: absolute;
    left: 0;
    top: 0;
    width: 1200px;
    height: 801px;
  }
  .word {
    position: absolute;
    margin: 0;
    display: flex;
    justify-content: space-between;
    color: var(--yellow);
    font-weight: 600;
    font-size: 166px;
    line-height: 1;
    text-shadow: -4px 3px 0 var(--ink);
  }
  .word--title { left: 88px; top: 24px; width: 1048px; }
  .word--artist { left: 228px; top: 632px; width: 780px; }
</style>
</head>
<body>
  <main class="cover">
    <div class="band band--top"></div>
    <div class="band band--top-post"></div>
    <div class="band band--left"></div>
    <div class="band band--right"></div>
    <div class="band band--foot"></div>

    <svg class="artist-photo" viewBox="0 0 1200 801" role="img" aria-label="Posterised portrait of the artist in a studded black beanie, long dark hair and denim jacket, hand raised to her head">
      <defs>
        <linearGradient id="portraitTone" x1="0" y1="0" x2="0" y2="1">
          <stop offset="0" stop-color="#050505"/>
          <stop offset="0.45" stop-color="#2a1a10"/>
          <stop offset="1" stop-color="#1d6f86"/>
        </linearGradient>
      </defs>
      <path fill="url(#portraitTone)" d="M600 62 C 520 62 455 110 440 190 C 430 240 430 330 440 400 C 410 470 400 520 380 560 C 300 580 240 620 210 700 L 175 801 L 1110 801 L 1070 700 C 1040 640 1000 600 960 580 L 930 470 L 880 360 L 840 300 L 790 270 L 770 190 C 750 110 680 62 600 62 Z"/>
    </svg>

    <h1 class="word word--title" aria-label="Glimmer">
      <span>G</span><span>L</span><span>I</span><span>M</span><span>M</span><span>E</span><span>R</span>
    </h1>
    <h2 class="word word--artist" aria-label="Relna">
      <span>R</span><span>E</span><span>L</span><span>N</span><span>A</span>
    </h2>
  </main>
</body>
</html>
```